Podcast graphics

We are working on a launch of a podcast for couples in the fourth quarter of relationship.Our goal is to help couples in the 4th quarter of their life experience powerful and positive relationships. (Focus Age: 55-70) Kestrel Hour may still be in career mode but beginning to wonder about retirement or "what's next" transitions. Some may choose conventional retirement or a transition to a different rhythm of life. These couples are active and have energy to work, volunteer, travel, and play. The focus is connecting resources and insights that will help them thrive in fourth quarter relationships. The Kestrel-Hour podcast is the resource for an intentional dynamic couple life. Exploring physical and emotional health, travel, relationships, life after employment and much more.

Target Market(s)

couples in the 4th quarter of their life experience powerful and positive relationships. (Focus Age: 55-70)

Logo Text

open to concepts but text should identify the podcast as Kestrel hour -

Requirements
Must have
• design specs in final artwork to meet podcast graphics standard of max 2048x2048
Nice to have
• high energy... the design will extend to a webpage for show notes and Facebook page
Should not have
• not thinking something with an image of a couple but open to concepts.

```html
<!DOCTYPE html>
<html lang="en">
<head>
<meta charset="utf-8">
<title>Kestrel Hour — Podcast Cover</title>
<link rel="stylesheet" href="https://fonts.googleapis.com/css2?family=Limelight&family=Montserrat:wght@800&display=swap">
<style>
  :root {
    --cream: #fbf0b4;
    --deep-red: #3a0004;
    --wine: #6e0a0e;
    --ember: #d83a1e;
    --flame: #f2a33a;
    --magenta: #c43a7a;
    --violet: #6a3bd0;
    --border-word: rgba(255, 235, 240, 0.72);
  }
  * { margin: 0; padding: 0; box-sizing: border-box; }
  html, body { width: 1200px; height: 1200px; overflow: hidden; background: #000; }
  .cover {
    position: relative;
    width: 1200px;
    height: 1200px;
    overflow: hidden;
    background:
      radial-gradient(circle at 0% 40%, var(--flame) 0%, transparent 30%),
      radial-gradient(circle at 100% 15%, var(--violet) 0%, transparent 35%),
      radial-gradient(circle at 100% 70%, var(--magenta) 0%, transparent 35%),
      radial-gradient(circle at 50% 100%, #f0607a 0%, transparent 40%),
      linear-gradient(135deg, var(--ember), #b0142a 50%, #8a1a60);
  }
  .border-word {
    position: absolute;
    font-family: "Montserrat", sans-serif;
    font-weight: 800;
    font-size: 96px;
    line-height: 1;
    letter-spacing: -1px;
    color: var(--border-word);
    white-space: nowrap;
  }
  .border-word--top { top: -18px; left: 78px; }
  .border-word--bottom { bottom: -22px; left: 144px; }
  .border-word--left {
    left: -14px; bottom: 0;
    transform-origin: left bottom;
    transform: rotate(-90deg) translate(0, 100%);
    width: 1200px;
  }
  .border-word--right {
    right: -14px; top: 0;
    transform-origin: right top;
    transform: rotate(90deg) translate(100%, 0);
    width: 1200px;
    text-align: left;
    display: flex;
    justify-content: space-between;
    padding-right: 20px;
  }
  .stage {
    position: absolute;
    left: 76px; top: 76px;
    width: 1048px; height: 1048px;
    background:
      radial-gradient(ellipse at 20% 50%, rgba(200, 190, 60, 0.35) 0%, transparent 30%),
      radial-gradient(ellipse at 60% 40%, rgba(140, 30, 30, 0.9) 0%, transparent 60%),
      linear-gradient(160deg, var(--wine) 0%, #8a1414 40%, var(--deep-red) 100%);
  }
  .show-title {
    position: absolute;
    left: 76px; top: 76px;
    width: 1048px; height: 1048px;
    display: flex;
    flex-direction: column;
    align-items: center;
    justify-content: center;
    gap: 70px;
    font-family: "Limelight", serif;
    color: var(--cream);
    text-align: center;
  }
  .show-title__first {
    font-size: 150px;
    line-height: 1;
    transform: scaleY(2.6);
    margin-top: 40px;
  }
  .show-title__second {
    font-size: 220px;
    line-height: 1;
    transform: scaleY(1.35);
    margin-top: 110px;
  }
</style>
</head>
<body>
  <main class="cover">
    <span class="border-word border-word--top">PHYSICAL HEALTH</span>
    <span class="border-word border-word--left">RETIREMENT WORK</span>
    <span class="border-word border-word--right"><span>EMOTIONS</span><span>TRAVEL</span></span>
    <span class="border-word border-word--bottom">RELATIONSHIPS</span>

    <div class="stage" role="img" aria-label="Long-exposure photograph of a guitar with swirling light trails in deep red, yellow and blue"></div>

    <h1 class="show-title">
      <span class="show-title__first">KESTREL</span>
      <span class="show-title__second">HOUR</span>
    </h1>
  </main>
</body>
</html>
```